KFO R Training Website

We need a website to post videos, blogs and other information or links.
We teach Jujitsu , combatives, Metaphysical Coaching. I want to tach online and in person. Silver Heron Institute Deals in several areas of Personal Protection and Coaching.
Training (Martial Arts / combative)
Emotional Intelligence
Leadership Development
Motivation
Our Log is attached.
Similar Websites to what we do ( we want to stand out better).
https://marcovelden.example/
https://raybusko.example/
https://summitfusionmentoring.example/
Industry/Entity Type
Training , Martial Arts, coaching
Coding
Coded - Design and coding required
Number of Pages Required
2 page
Look and feel

```html
<!DOCTYPE html>
<html lang="en">
<head>
<meta charset="utf-8">
<title>Silver Heron Institute</title>
<link href="https://fonts.googleapis.com/css2?family=Montserrat:wght@600;700;800&family=Roboto:wght@400;500;700&display=swap" rel="stylesheet">
<style>
:root{
  --red:#d0021b;
  --black:#000;
  --panel:#0c0e0e;
  --card:#121212;
  --white:#fff;
  --muted:#cfcfcf;
  --dim:#6c6c6c;
  --line:#2a2a2a;
  --meta:#1b0206;
}
*{margin:0;padding:0;box-sizing:border-box}
html,body{width:1200px;height:4713px;overflow:hidden;background:var(--black);color:var(--white);font-family:"Roboto",Arial,sans-serif}
.page{position:relative;width:1200px;height:4713px}
.abs{position:absolute}
a{color:inherit;text-decoration:none}

.topbar{left:0;top:0;width:1200px;height:40px;background:var(--red);font-size:14px;font-weight:500}
.topbar .item{position:absolute;top:12px;display:flex;align-items:center;gap:8px;white-space:nowrap}
.topbar .sep{position:absolute;top:11px}

.nav{left:0;top:40px;width:1200px;height:90px;background:var(--black)}
.brand{position:absolute;left:104px;top:48px;width:182px;height:118px;background:var(--black);border:1px solid #333;display:flex;flex-direction:column;align-items:center;justify-content:center;gap:8px;z-index:3}
.brand .mark{width:40px;height:40px;background:var(--white)}
.brand .name{font-family:"Montserrat",sans-serif;font-weight:700;font-size:15px;color:var(--white);letter-spacing:.5px;text-align:center;line-height:1.2}
.menu{position:absolute;top:38px;font-size:14px;font-weight:700}
.menu a{position:absolute;white-space:nowrap}
.menu .active{color:var(--red)}
.search{position:absolute;left:1048px;top:32px;width:36px;height:36px;border-radius:50%;background:var(--red)}

.hero{left:0;top:130px;width:1200px;height:644px;background:linear-gradient(90deg,#151312 0%,#3b302a 45%,#6e625a 70%,#3a3431 100%)}
.hero-shade{left:0;top:130px;width:1200px;height:644px;background:linear-gradient(90deg,rgba(0,0,0,.75) 0%,rgba(0,0,0,.35) 55%,rgba(0,0,0,.05) 100%)}
.welcome{left:112px;top:294px;font-family:"Montserrat",sans-serif;font-weight:700;font-size:29px;letter-spacing:1px}
.hero-title{left:112px;top:350px;font-family:"Montserrat",sans-serif;font-weight:800;font-size:45px;line-height:52px;letter-spacing:1px}
.hero-text{left:112px;top:478px;width:520px;font-size:16.5px;line-height:25px}
.btn{display:flex;align-items:center;justify-content:center;gap:10px;background:var(--red);border-radius:24px;font-size:13.5px;font-weight:700;color:var(--white);text-transform:uppercase}
.hero-btn{left:112px;top:556px;width:190px;height:46px}

.eyebrow{left:0;width:1200px;font-family:"Montserrat",sans-serif;font-weight:600;font-size:18px;color:var(--red);display:flex;justify-content:center;align-items:center;gap:14px}
.eyebrow::before,.eyebrow::after{content:"";width:52px;height:2px;background:var(--red)}
.heading{left:0;width:1200px;text-align:center;font-family:"Montserrat",sans-serif;font-weight:700;font-size:29px;letter-spacing:1px}
.intro{left:130px;width:940px;text-align:center;font-size:14px;line-height:23px;color:var(--muted)}

.card{top:1048px;width:311px;height:397px;background:var(--card);border-radius:14px;overflow:hidden}
.card .photo{position:absolute;left:6px;top:6px;right:6px;height:200px;border-radius:10px 10px 0 0}
.play{position:absolute;width:36px;height:36px;border-radius:50%;background:var(--red);display:flex;align-items:center;justify-content:center}
.card .play{left:50%;top:88px;margin-left:-18px}
.card h3{position:absolute;left:0;right:0;top:230px;text-align:center;font-size:19px;font-weight:700}
.card p{position:absolute;left:20px;right:20px;top:266px;font-size:13.5px;line-height:20px;text-align:justify;text-align-last:center;color:var(--muted)}
.card .meta{position:absolute;left:0;right:0;bottom:0;height:46px;background:var(--meta);display:flex;align-items:center;justify-content:center;gap:22px;font-size:13px;font-weight:700}
.card .meta span{display:flex;align-items:center;gap:8px}
.card.featured{box-shadow:inset 0 0 0 2px var(--red)}
.card.featured .meta{background:var(--red)}
.badge{position:absolute;right:18px;top:18px;background:var(--red);font-size:10px;font-weight:700;padding:4px 10px}

.about{left:0;top:1567px;width:1200px;height:555px;background:var(--panel)}
.about-mark{left:155px;top:1637px;width:363px;height:417px;display:flex;flex-direction:column;align-items:center;justify-content:center;gap:24px}
.about-mark .sq{width:120px;height:120px;background:var(--white)}
.about-mark .name{font-family:"Montserrat",sans-serif;font-weight:700;font-size:30px;text-align:center;line-height:38px}
.about .eb{position:absolute;left:602px;top:63px;font-family:"Montserrat",sans-serif;font-weight:600;font-size:18px;color:var(--red);display:flex;align-items:center;gap:14px}
.about .eb::after{content:"";width:52px;height:2px;background:var(--red)}
.about h2{position:absolute;left:602px;top:92px;font-family:"Montserrat",sans-serif;font-size:29px;font-weight:700;letter-spacing:1px}
.about p{position:absolute;left:602px;top:150px;width:488px;font-size:14px;line-height:24px;text-align:justify;color:var(--muted)}
.about .btn{position:absolute;left:602px;top:438px;width:188px;height:48px}

.course{top:2383px;width:240px;text-align:center}
.course .emblem{width:130px;height:168px;margin:0 auto;background:var(--red);border-radius:10px}
.course h4{margin-top:22px;font-size:17px;font-weight:700}
.course p{margin:20px auto 0;width:200px;font-size:13.5px;line-height:21px;color:var(--muted)}
.courses-end{left:0;top:2753px;width:1200px;height:1px;background:#161616}

.video{overflow:hidden}
.video .play{left:50%;top:50%;margin:-18px 0 0 -18px}
.video-btn{left:505px;top:3416px;width:190px;height:48px}

.post-img{position:relative}
.date{position:absolute;background:var(--red);font-size:13px;font-weight:700;padding:8px 16px}
.post-text{background:#101010;padding:24px 22px}
.post-text h5{font-size:15px;font-weight:700;line-height:24px}
.post-text .rule{width:34px;height:2px;background:var(--red);margin:14px 0 12px}
.post-text p{font-size:12px;line-height:20px;color:var(--dim)}
.post-text .more{margin-top:12px;font-size:12px;font-weight:700;color:var(--red);text-decoration:underline}

.news-title{left:112px;top:4240px;font-family:"Montserrat",sans-serif;font-weight:700;font-size:23px;letter-spacing:.5px}
.news-sub{left:112px;top:4282px;font-size:15px;color:var(--muted)}
.news-input{left:561px;top:4250px;width:353px;height:46px;background:var(--black);border:1px solid #333;display:flex;align-items:center;gap:14px;padding-left:20px;font-size:14px;color:var(--muted)}
.news-btn{left:914px;top:4250px;width:172px;height:46px;background:var(--red);font-size:14px;font-weight:700;display:flex;align-items:center;justify-content:center}
.foot-line{left:112px;top:4343px;width:974px;height:1px;background:var(--line)}

.foot-brand{left:112px;top:4372px;width:240px}
.foot-brand .sq{width:70px;height:70px;background:var(--white);margin-left:60px}
.foot-brand .name{margin-top:14px;font-family:"Montserrat",sans-serif;font-weight:700;font-size:22px;line-height:26px}
.foot-about{left:112px;top:4546px;width:390px;font-size:14px;line-height:24px;color:var(--muted)}
.foot-divider{top:4380px;width:1px;height:240px;background:var(--line)}
.foot-h{font-size:16px;font-weight:700}
.foot-h::after{content:"";display:block;width:40px;height:2px;background:var(--red);margin-top:12px}
.links{left:582px;top:4440px;list-style:none;font-size:13px;color:var(--muted)}
.links li{height:27px;display:flex;align-items:center;gap:16px}
.links li::before{content:"";width:5px;height:5px;border-radius:50%;background:var(--red)}
.contact-row{left:794px;display:flex;gap:20px;align-items:flex-start}
.contact-row .lab{font-size:12px;color:var(--red);text-transform:uppercase}
.contact-row .val{font-size:14px;color:var(--white);margin-top:3px;white-space:nowrap}
.bottom{left:0;top:4664px;width:1200px;height:49px;background:var(--red);font-size:14px;display:flex;align-items:center;justify-content:center}
</style>
</head>
<body>
<div class="page">

  <div class="abs topbar">
    <div class="item" style="left:112px">
      <svg width="15" height="11" viewBox="0 0 15 11"><rect width="15" height="11" rx="1" fill="#fff"/><path d="M0 1 7.5 6 15 1" stroke="#d0021b" stroke-width="1.4" fill="none"/></svg>
      <span>info@silverheron.example</span>
    </div>
    <span class="sep" style="left:380px">|</span>
    <div class="item" style="left:414px">
      <svg width="13" height="13" viewBox="0 0 24 24"><path fill="#fff" d="M6.6 10.8a15 15 0 0 0 6.6 6.6l2.2-2.2a1 1 0 0 1 1-.25 11.4 11.4 0 0 0 3.6.57 1 1 0 0 1 1 1V20a1 1 0 0 1-1 1A17 17 0 0 1 3 4a1 1 0 0 1 1-1h3.5a1 1 0 0 1 1 1c0 1.25.2 2.45.57 3.6a1 1 0 0 1-.25 1z"/></svg>
      <span>+ 1 555 014 7720</span>
    </div>
    <div class="item" style="left:844px">
      <svg width="12" height="12" viewBox="0 0 24 24"><circle cx="12" cy="7" r="5" fill="#fff"/><path d="M2 24c0-6 4.5-9 10-9s10 3 10 9z" fill="#fff"/></svg>
      <span>LOGIN</span>
    </div>
    <span class="sep" style="left:924px">|</span>
    <div class="item" style="left:948px">
      <span>SEE OUR &nbsp;COURSES</span>
      <svg width="13" height="13" viewBox="0 0 24 24"><circle cx="12" cy="12" r="11" fill="#fff"/><path d="M10 7l5 5-5 5" stroke="#d0021b" stroke-width="3" fill="none"/></svg>
    </div>
  </div>

  <div class="abs nav">
    <nav class="menu">
      <a class="active" style="left:426px">Home</a>
      <a style="left:501px">About</a>
      <a style="left:577px">Services</a>
      <a style="left:670px">Products</a>
      <a style="left:765px">Media</a>
      <a style="left:841px">Content</a>
      <a style="left:929px">Contact</a>
    </nav>
    <div class="search">
      <svg width="36" height="36" viewBox="0 0 36 36"><circle cx="17" cy="17" r="5" stroke="#fff" stroke-width="2" fill="none"/><path d="M21 21l4 4" stroke="#fff" stroke-width="2.4"/></svg>
    </div>
  </div>
  <div class="brand">
    <div class="mark"></div>
    <div class="name">SILVER HERON<br>INSTITUTE</div>
  </div>

  <div class="abs hero" role="img" aria-label="Photo of a smiling woman in conversation with a man across a desk"></div>
  <div class="abs hero-shade"></div>
  <div class="abs welcome">WELCOME TO</div>
  <h1 class="abs hero-title">SILVER HERON<br>INSTITUTE</h1>
  <p class="abs hero-text">Lorem ipsum dolor sit amet, consectetur adipiscing elit, sed do eiusmod tempor incididunt ut labore et dolore</p>
  <a class="abs btn hero-btn">Book your call
    <svg width="13" height="13" viewBox="0 0 14 14"><rect x="1" y="2" width="12" height="11" fill="none" stroke="#fff" stroke-width="1.4"/><path d="M1 5h12M4 0v3M10 0v3" stroke="#fff" stroke-width="1.4"/></svg>
  </a>

  <div class="abs eyebrow" style="top:860px">OUR SERVICES</div>
  <h2 class="abs heading" style="top:886px">WHAT WE TEACH</h2>
  <p class="abs intro" style="top:940px">Sed ut perspiciatis unde omnis iste natus error sit voluptatem accusantium doloremque laudantium, totam rem aperiam, eaque ipsa quae ab illo inventore veritatis et quasi architecto beatae vitae dicta sunt explicabo.</p>

  <div class="abs card" style="left:110px">
    <div class="photo" role="img" aria-label="Photo of a jujitsu class kneeling on training mats" style="background:linear-gradient(135deg,#b9a690,#e6e2dc 60%,#cfc8bf)"></div>
    <div class="play"><svg width="12" height="14" viewBox="0 0 12 14"><path d="M1 0l11 7-11 7z" fill="#fff"/></svg></div>
    <h3>Jujitsu</h3>
    <p>Lorem ipsum dolor sit amet, consectetur adipiscing elit, sed do eiusmod tempor incididunt ut labore et dolore</p>
    <div class="meta"><span>⏲ 45 Min</span><span>|</span><span>👤 Wade Tanner</span></div>
  </div>
  <div class="abs card featured" style="left:444px">
    <div class="photo" role="img" aria-label="Photo of two women sparring with boxing gloves on mats" style="background:linear-gradient(135deg,#9fa7a6,#d8dad5 55%,#7b8a6a)"></div>
    <div class="badge">FREE</div>
    <div class="play"><svg width="12" height="14" viewBox="0 0 12 14"><path d="M1 0l11 7-11 7z" fill="#fff"/></svg></div>
    <h3>Combative</h3>
    <p>Lorem ipsum dolor sit amet, consectetur adipiscing elit, sed do eiusmod tempor incididunt ut labore et dolore</p>
    <div class="meta"><span>⏲ 45 Min</span><span>|</span><span>👤 Wade Tanner</span></div>
  </div>
  <div class="abs card" style="left:779px">
    <div class="photo" role="img" aria-label="Photo of women meditating in a bright room" style="background:linear-gradient(135deg,#c6c3bd,#e9e7e2 55%,#b5b0a8)"></div>
    <div class="play"><svg width="12" height="14" viewBox="0 0 12 14"><path d="M1 0l11 7-11 7z" fill="#fff"/></svg></div>
    <h3>Metaphysical Coaching</h3>
    <p>Lorem ipsum dolor sit amet, consectetur adipiscing elit, sed do eiusmod tempor incididunt ut labore et dolore</p>
    <div class="meta"><span>⏲ 45 Min</span><span>|</span><span>👤 Wade Tanner</span></div>
  </div>

  <section class="abs about">
    <div class="eb">ABOUT US</div>
    <h2>WHO WE ARE</h2>
    <p>Sed ut perspiciatis unde omnis iste natus error sit voluptatem accusantium doloremque laudantium, totam rem aperiam, eaque ipsa quae ab illo inventore veritatis et quasi architecto beatae vitae dicta sunt explicabo. Nemo enim ipsam voluptatem quia voluptas sit aspernatur aut odit aut fugit, sed quia consequuntur magni dolores eos qui ratione voluptatem sequi nesciunt.Sed ut perspiciatis unde omnis iste natus error sit voluptatem accusantium doloremque laudantium, totam rem aperiam, eaque ipsa quae ab illo inventore veritatis et quasi architecto beatae vitae dicta sunt explicabo. Nemo enim ipsam voluptatem quia voluptas sit aspernatur aut odit aut fugit, sed quia consequuntur magni dolores eos qui ratione voluptatem sequi nesciunt.</p>
    <a class="btn">Book your call
      <svg width="13" height="13" viewBox="0 0 14 14"><rect x="1" y="2" width="12" height="11" fill="none" stroke="#fff" stroke-width="1.4"/><path d="M1 5h12M4 0v3M10 0v3" stroke="#fff" stroke-width="1.4"/></svg>
    </a>
  </section>
  <div class="abs about-mark">
    <div class="sq"></div>
    <div class="name">SILVER HERON<br>INSTITUTE</div>
  </div>

  <div class="abs eyebrow" style="top:2209px">OUR DEALS</div>
  <h2 class="abs heading" style="top:2235px">OUR COURSES</h2>
  <p class="abs intro" style="top:2290px">Sed ut perspiciatis unde omnis iste natus error sit voluptatem accusantium doloremque laudantium, totam rem aperiam, eaque ipsa quae ab illo inventore veritatis et quasi architecto beatae vitae dicta sunt explicabo.</p>

  <div class="abs course" style="left:109px">
    <div class="emblem" role="img" aria-label="Red emblem for the training course"></div>
    <h4>Training</h4>
    <p>Sed ut perspiciatis unde omnis iste natus error sit voluptat</p>
  </div>
  <div class="abs course" style="left:356px">
    <div class="emblem" role="img" aria-label="Red emblem for the emotional intelligence course"></div>
    <h4>Emotional Intelligence</h4>
    <p>Sed ut perspiciatis unde omnis iste natus error sit voluptat</p>
  </div>
  <div class="abs course" style="left:602px">
    <div class="emblem" role="img" aria-label="Red emblem for the leadership development course"></div>
    <h4>Leadership Development</h4>
    <p>Sed ut perspiciatis unde omnis iste natus error sit voluptat</p>
  </div>
  <div class="abs course" style="left:849px">
    <div class="emblem" role="img" aria-label="Red emblem for the motivation course"></div>
    <h4>Motivation</h4>
    <p>Sed ut perspiciatis unde omnis iste natus error sit voluptat</p>
  </div>
  <div class="abs courses-end"></div>

  <div class="abs eyebrow" style="top:2829px">PROGRAMS</div>
  <h2 class="abs heading" style="top:2855px">OUR VIDEOS</h2>
  <p class="abs intro" style="top:2910px">Sed ut perspiciatis unde omnis iste natus error sit voluptatem accusantium doloremque laudantium, totam rem aperiam, eaque ipsa quae ab illo inventore veritatis et quasi architecto beatae vitae dicta sunt explicabo.</p>

  <div class="abs video" style="left:112px;top:3047px;width:272px;height:253px;background:linear-gradient(135deg,#6b7a5a,#c4c0b6 60%,#8a8276)" role="img" aria-label="Photo of a woman on the phone at a desk with plants">
    <div class="play"><svg width="12" height="14" viewBox="0 0 12 14"><path d="M1 0l11 7-11 7z" fill="#fff"/></svg></div>
  </div>
  <div class="abs video" style="left:816px;top:3047px;width:272px;height:253px;background:linear-gradient(135deg,#d9d3cb,#a89a8c 60%,#6f6459)" role="img" aria-label="Photo of a smiling woman working on a laptop">
    <div class="play"><svg width="12" height="14" viewBox="0 0 12 14"><path d="M1 0l11 7-11 7z" fill="#fff"/></svg></div>
  </div>
  <div class="abs video" style="left:384px;top:3020px;width:432px;height:311px;background:linear-gradient(135deg,#4c5058,#8a8f98 50%,#3b4a6a)" role="img" aria-label="Photo of a man in glasses writing at a desk">
    <div class="play"><svg width="12" height="14" viewBox="0 0 12 14"><path d="M1 0l11 7-11 7z" fill="#fff"/></svg></div>
  </div>
  <a class="abs btn video-btn">View all videos
    <svg width="13" height="13" viewBox="0 0 24 24"><circle cx="12" cy="12" r="11" fill="#fff"/><path d="M10 7l5 5-5 5" stroke="#d0021b" stroke-width="3" fill="none"/></svg>
  </a>

  <div class="abs eyebrow" style="top:3540px">RESOURCES</div>
  <h2 class="abs heading" style="top:3566px">LATEST BLOG</h2>

  <div class="abs" style="left:113px;top:3663px;width:322px">
    <div class="post-img" style="height:216px;background:linear-gradient(135deg,#bfb6ab,#e6e3df 55%,#9a8f84)" role="img" aria-label="Photo of a woman in a white blazer working on a laptop">
      <div class="date" style="right:10px;top:10px">JUNE 2022</div>
    </div>
    <div class="post-text" style="height:204px">
      <h5>Lorem ipsum dolor sit amet, consec tetur adipiscing</h5>
      <div class="rule"></div>
      <p>Sed ut perspiciatis unde omnis iste natus error sit voluptatem accusantium doloremque</p>
      <div class="more">LEARN MORE ➔</div>
    </div>
  </div>
  <div class="abs" style="left:435px;top:3663px;width:326px">
    <div class="post-text" style="height:201px">
      <h5>Lorem ipsum dolor sit amet, consec tetur adipiscing</h5>
      <div class="rule"></div>
      <p>Sed ut perspiciatis unde omnis iste natus error sit voluptatem accusantium doloremque</p>
      <div class="more">LEARN MORE ➔</div>
    </div>
    <div class="post-img" style="height:219px;background:linear-gradient(135deg,#3d3a3a,#8f857a 55%,#c9c2b8)" role="img" aria-label="Photo of a woman on a video call on a laptop">
      <div class="date" style="left:110px;bottom:6px">JUNE 2022</div>
    </div>
  </div>
  <div class="abs" style="left:761px;top:3663px;width:325px">
    <div class="post-img" style="height:216px;background:linear-gradient(135deg,#d8d2ca,#a99b8a 55%,#efece7)" role="img" aria-label="Photo of a smiling woman typing on a laptop">
      <div class="date" style="right:10px;top:10px">JUNE 2022</div>
    </div>
    <div class="post-text" style="height:204px">
      <h5>Lorem ipsum dolor sit amet, consec tetur adipiscing</h5>
      <div class="rule"></div>
      <p>Sed ut perspiciatis unde omnis iste natus error sit voluptatem accusantium doloremque</p>
      <div class="more">LEARN MORE ➔</div>
    </div>
  </div>

  <div class="abs news-title">SUBSCRIBE OUR NEWSLETTER</div>
  <div class="abs news-sub">Lorem ipsum dolor sit amet, consectetur adipiscing elit</div>
  <div class="abs news-input">
    <svg width="15" height="11" viewBox="0 0 15 11"><rect width="15" height="11" rx="1" fill="#fff"/><path d="M0 1 7.5 6 15 1" stroke="#000" stroke-width="1.4" fill="none"/></svg>
    <span>Enter Your Email</span>
  </div>
  <div class="abs news-btn">SUBSCRIBE NOW</div>
  <div class="abs foot-line"></div>

  <div class="abs foot-brand">
    <div class="sq"></div>
    <div class="name">SILVER HERON<br>INSTITUTE</div>
  </div>
  <p class="abs foot-about">Sed ut perspiciatis unde omnis iste natus errorvoluptatem accusantium doloremque laudantium, totam remaperiam, eaque ipsa quae ab illo inventore veritatis</p>
  <div class="abs foot-divider" style="left:530px"></div>
  <div class="abs foot-divider" style="left:746px"></div>

  <div class="abs foot-h" style="left:582px;top:4378px">Quick Links</div>
  <ul class="abs links">
    <li>Home</li><li>About</li><li>Our Coaching</li><li>Our Services</li><li>Videos</li><li>Blog</li><li>Contact</li>
  </ul>

  <div class="abs foot-h" style="left:794px;top:4378px">Contact Us</div>
  <div class="abs contact-row" style="top:4444px">
    <svg width="18" height="28" viewBox="0 0 18 28"><rect x="1" y="1" width="16" height="26" rx="2" fill="none" stroke="#fff" stroke-width="2"/><circle cx="9" cy="22" r="1.6" fill="#fff"/></svg>
    <div><div class="lab">Phone No :</div><div class="val" style="font-size:18px;font-weight:500">+ 1 555 014 7720</div></div>
  </div>
  <div class="abs contact-row" style="top:4504px">
    <svg width="26" height="20" viewBox="0 0 26 20"><rect x="1" y="1" width="24" height="18" fill="none" stroke="#fff" stroke-width="2"/><path d="M1 1l12 10L25 1M1 19l9-9M25 19l-9-9" stroke="#fff" stroke-width="2" fill="none"/></svg>
    <div><div class="lab">E-mail :</div><div class="val">hello@silverheron.example</div></div>
  </div>
  <div class="abs contact-row" style="top:4562px">
    <svg width="22" height="28" viewBox="0 0 22 28"><path d="M11 0C5 0 0 5 0 11c0 8 11 17 11 17s11-9 11-17C22 5 17 0 11 0z" fill="#fff"/><circle cx="11" cy="11" r="4" fill="#000"/></svg>
    <div><div class="lab">Location :</div><div class="val">62 Larchmont Way , Fairview , United States</div></div>
  </div>

  <div class="abs bottom">© 2022 Silver Heron Institute. All Rights Reserved</div>
</div>
</body>
</html>
```